New Year

Contemporary Art company (ART DEALER) would like to send a WEB greeting Card for the Jewish new year. It should be modern and artistic. The design should not contain any copyright artworks. It should be meaningful for the time of the year. (JEWISH NEW YEAR) Rosh Hashanah! It is customary to send a greeting that says "L' Shana Tova!" and all wishes greetings encompass sweet new year (honey), health, etc. Shofar, art, beautiful life very contemporary and modern.

Company logo will be provided to best designs.
NOTE: DEADLINE is 09/17/2014 by mistake the system placed 09/19/2014

Reason: The proposals received do not meet the requirement. This is a Contemporary Art Company, thus the design should be very modern, contemporary. No ITALICS, or cursive fonts, Fresh and Cool designs.

Target Market(s)

Upscale art buyers, well educated and luxury consumers

Industry/Entity Type

It Company

Font styles to use
Serif
Sans Serif
Other font styles liked:
• Trade Gothic LT Std

Requirements
Must have
• Space for Company Logo (provided to winner)
• email address, telephone and address of our business.
• IS AN EMAIL GREETING CARD. Thus, it must be ready to be sent via constant contact, regular email and easily to see on a computer screen or mobile device.
Nice to have
• Meaning full, something that will make people and recipients happy of doing business with. Font: Trade Gothic LT Std
Should not have
• Any copy rights images of images

```html
<!DOCTYPE html>
<html lang="en">
<head>
<meta charset="utf-8">
<title>Rosh Hashanah Greeting</title>
<link rel="stylesheet" href="https://fonts.googleapis.com/css2?family=Roboto+Condensed:wght@300;400;700&display=swap">
<style>
  :root {
    --paper: #fdf9ea;
    --ink: #7a2410;
    --ink-soft: #e9cdb8;
    --logo-text: #fdf9ea;
  }
  * { margin: 0; padding: 0; box-sizing: border-box; }
  html, body {
    width: 846px;
    height: 1200px;
    overflow: hidden;
    background: var(--paper);
  }
  .card {
    position: relative;
    width: 846px;
    height: 1200px;
    background: var(--paper);
    color: var(--ink);
    font-family: "Roboto Condensed", "Arial Narrow", sans-serif;
  }
  .symbol-grid {
    position: absolute;
    left: 0;
    top: 0;
  }
  .title {
    position: absolute;
    left: 0;
    width: 100%;
    top: 690px;
    text-align: center;
    font-weight: 300;
    font-size: 84px;
    line-height: 1;
    letter-spacing: -1px;
  }
  .greeting {
    position: absolute;
    left: 0;
    width: 100%;
    top: 842px;
    text-align: center;
    font-size: 31px;
    line-height: 39px;
    font-weight: 400;
  }
  .greeting-lead {
    font-weight: 700;
    font-size: 29px;
  }
  .logo-block {
    position: absolute;
    left: 350px;
    top: 1060px;
    width: 152px;
    height: 80px;
    background: var(--ink);
    color: var(--logo-text);
    display: flex;
    align-items: center;
    justify-content: center;
    font-size: 29px;
    font-weight: 400;
  }
</style>
</head>
<body>
  <main class="card">
    <svg class="symbol-grid" width="846" height="640" viewBox="0 0 846 640" aria-hidden="false">
      <g fill="none" stroke="var(--ink)" stroke-width="4">
        <circle cx="242" cy="202" r="69"/>
        <circle cx="422" cy="202" r="69"/>
        <circle cx="604" cy="202" r="69"/>
        <circle cx="242" cy="364" r="69"/>
        <circle cx="422" cy="364" r="69"/>
        <circle cx="604" cy="364" r="69"/>
        <circle cx="242" cy="528" r="69"/>
        <circle cx="422" cy="528" r="69"/>
        <circle cx="604" cy="528" r="69"/>
      </g>
      <g fill="var(--ink-soft)">
        <circle cx="242" cy="202" r="48" role="img" aria-label="Menorah symbol"/>
        <circle cx="422" cy="202" r="48" role="img" aria-label="Pomegranate tree symbol"/>
        <circle cx="604" cy="202" r="48" role="img" aria-label="Honey dippers and honeycomb symbol"/>
        <circle cx="422" cy="364" r="48" role="img" aria-label="Star of David symbol"/>
        <circle cx="604" cy="364" r="48" role="img" aria-label="Shofar horn symbol"/>
      </g>
    </svg>

    <h1 class="title">ROSH HASHANAH</h1>

    <p class="greeting">
      <span class="greeting-lead">L’Shana Tova!</span><br>
      Wishing you a new year that brings<br>
      fulfilment and happiness,<br>
      peace and prosperity
    </p>

    <div class="logo-block">LOGO</div>
  </main>
</body>
</html>
```